Public Speaking Book for aspiring, ambitious speakers

I'm looking for a 6x9 book cover (Brevora standard) as well as ebook and audiobook formats.

I'm looking for orange font on a white background as these are my brand colours.

Feel free to use some yellow and gold too if you deem it appropriate.

Title: Climb and Kindle
Subtitle: Find Your Voice. Tell Your Story. Share your Message.
Author: Tobias Wenlock

I would like to have a picture of a female speaker on the front cover.

Alternatively, some kind of image that symbolises public speaking like a microphone, podium etc

Target Market(s)

Aspiring professional speakers

Colors
f78f20

Requirements
Must have
• Correct spelling!
Nice to have
• A logo or picture that fits the theme, but no pressure if you can't think of anything
Should not have
• No men in suits please. I don't want this to have a 1980s corporate look.

```html
<!DOCTYPE html>
<html lang="en">
<head>
<meta charset="UTF-8">
<title>Climb and Kindle — Book Cover</title>
<link href="https://fonts.googleapis.com/css2?family=Montserrat:wght@300;600;800;900&display=swap" rel="stylesheet">
<style>
  :root {
    --page-bg: #eeeeee;
    --cover-white: #ffffff;
    --cover-mist: #f6f3ee;
    --brand-orange: #f78f20;
    --gold-soft: #f6c35a;
    --gold-pale: #fbe3b4;
    --author-ink: #1c1c1c;
  }
  * { margin: 0; padding: 0; box-sizing: border-box; }
  html, body {
    width: 1200px;
    height: 1200px;
    overflow: hidden;
    background: var(--page-bg);
  }
  .canvas {
    width: 1200px;
    height: 1200px;
    display: flex;
    align-items: center;
    justify-content: center;
  }
  .book-cover {
    position: relative;
    width: 680px;
    height: 1020px;
    background: linear-gradient(180deg, var(--cover-white) 0%, var(--cover-mist) 100%);
    overflow: hidden;
    font-family: "Montserrat", sans-serif;
    box-shadow: 0 10px 30px rgba(0,0,0,0.12);
  }
  .title-block {
    position: absolute;
    top: 80px;
    left: 0;
    right: 0;
    text-align: center;
    color: var(--brand-orange);
    text-transform: uppercase;
    line-height: 0.9;
  }
  .title-main {
    display: block;
    font-weight: 900;
    font-size: 124px;
    letter-spacing: -0.01em;
  }
  .title-joiner {
    display: block;
    font-weight: 300;
    font-size: 76px;
    margin: 8px 0 6px;
  }
  .speaker-art {
    position: absolute;
    top: 470px;
    left: 90px;
    width: 500px;
    height: 300px;
    border-radius: 6px;
    background:
      radial-gradient(ellipse 30% 45% at 50% 45%, var(--gold-soft), transparent 75%),
      radial-gradient(ellipse 70% 60% at 50% 60%, var(--gold-pale), transparent 80%),
      linear-gradient(180deg, #fff6e6 0%, #fde9c8 100%);
  }
  .subtitle {
    position: absolute;
    top: 806px;
    left: 40px;
    right: 40px;
    text-align: center;
    color: var(--brand-orange);
    font-weight: 600;
    font-size: 22px;
    letter-spacing: 0.06em;
    line-height: 1.4;
    text-transform: uppercase;
  }
  .author {
    position: absolute;
    top: 920px;
    left: 0;
    right: 0;
    text-align: center;
    color: var(--author-ink);
    font-weight: 800;
    font-size: 42px;
    letter-spacing: 0.02em;
  }
</style>
</head>
<body>
  <main class="canvas">
    <section class="book-cover">
      <h1 class="title-block">
        <span class="title-main">Climb</span>
        <span class="title-joiner">and</span>
        <span class="title-main">Kindle</span>
      </h1>
      <div class="speaker-art" role="img" aria-label="Photo of a female speaker on stage at a microphone, warm golden light"></div>
      <p class="subtitle">Find Your Voice. Tell Your Story.<br>Share Your Message.</p>
      <p class="author">Tobias Wenlock</p>
    </section>
  </main>
</body>
</html>
```